Roofing Company Realtor Marketing Flyer

We would like a design for marketing material aimed at realtors. We are seeking to build relationships with local realtors to ensure that both sellers and buyers are happy and confident with their roofing systems through roof inspections, Dry-Seal certification, roof repairs, and replacements if necessary.

There are three points that must be included:
1. Home inspectors are generalists. We are roof experts that specialize in diagnosing and fixing roofing problems.
2. We offer "Dry Seal" certification to offer peace of mind to homeowners.
3. We offer referral bonuses for realtors.

Target Market(s)

Realtors

Industry/Entity Type

Roofing

Font styles to use
Sans Serif

Colors

Designer to choose colors to be used in the design.

Requirements
Must have
• Must be double-sided.
• Must be similar to current marketing materials design. See website http://gablecrestmo.com and attached images for details.
• We would also like a "fanned out" version of our Sample Inspection Report showing glimpses of some of the images on the later pages (See attached documents).

```html
<!DOCTYPE html>
<html lang="en">
<head>
<meta charset="utf-8">
<title>Gable Crest – Realtor Flyer</title>
<link rel="stylesheet" href="https://fonts.googleapis.com/css2?family=Open+Sans:wght@400;600;700&display=swap">
<style>
  :root {
    --orange: #f58a1f;
    --orange-deep: #e5761a;
    --ink: #222222;
    --text: #333333;
    --grey-band: #d3d3d3;
    --bar: #353535;
    --bar-alt: #5a5a5a;
    --white: #ffffff;
    --ring: #5d5d5d;
  }
  * { margin: 0; padding: 0; box-sizing: border-box; }
  html, body { width: 810px; height: 1200px; overflow: hidden; background: #ffffff; }
  body { font-family: "Open Sans", Arial, sans-serif; color: var(--text); }
  .flyer { position: relative; width: 810px; height: 1200px; background: var(--white); overflow: hidden; }

  .brand { position: absolute; left: 38px; top: 38px; display: flex; align-items: center; gap: 12px; }
  .brand-mark { width: 18px; height: 18px; border-radius: 50%; background: var(--orange); }
  .brand-name { font-size: 50px; font-weight: 600; color: var(--orange); letter-spacing: -0.5px; line-height: 1; }
  .website { position: absolute; right: 26px; top: 44px; font-size: 21px; color: var(--ink); }
  .website b { color: var(--orange); font-weight: 600; }

  .hero { position: absolute; left: 0; top: 0; width: 810px; height: 900px; }

  .services-tab { position: absolute; left: 404px; top: 518px; width: 406px; height: 56px;
    background: var(--orange); border-radius: 14px 0 0 14px; color: var(--white);
    font-size: 36px; line-height: 56px; padding-left: 52px; }

  .services { position: absolute; left: 420px; top: 608px; height: 252px; border-left: 2px solid #bbbbbb;
    list-style: none; padding-left: 24px; }
  .services li { display: flex; align-items: center; gap: 22px; height: 63px; font-size: 27px; color: var(--ink); }
  .services svg { width: 42px; height: 42px; flex: none; }

  .pitch { position: absolute; left: 26px; top: 700px; width: 380px; }
  .pitch h2 { font-size: 38px; font-weight: 700; line-height: 44px; color: var(--ink); letter-spacing: -0.3px; }
  .pitch h2 span { display: block; color: var(--orange); }
  .pitch p { margin-top: 8px; font-size: 20.5px; line-height: 31px; text-transform: uppercase; color: var(--text); }

  .offer { position: absolute; left: 0; top: 935px; width: 810px; height: 196px; background: var(--grey-band); text-align: center; }
  .offer-tag { position: absolute; left: 287px; top: -22px; width: 230px; height: 46px; background: var(--orange);
    color: var(--ink); font-size: 30px; font-weight: 600; line-height: 46px;
    clip-path: polygon(0 0, 100% 0, 94% 50%, 100% 100%, 0 100%, 6% 50%); }
  .offer-line { display: inline-block; font-weight: 600; color: var(--ink); border-bottom: 2px solid #6a6a6a; }
  .offer-line.one { margin-top: 46px; font-size: 33px; line-height: 38px; border: none; }
  .offer-line.two { font-size: 31px; line-height: 40px; padding: 0 6px 2px; }
  .offer-line.three { margin-top: 18px; font-size: 37px; line-height: 46px; padding: 0 6px 2px; }

  .cta-bar { position: absolute; left: 0; top: 1137px; width: 810px; height: 63px; background: var(--bar-alt); }
  .cta-left { position: absolute; left: 0; top: 0; width: 440px; height: 63px; background: var(--bar);
    clip-path: polygon(0 0, 100% 0, 96% 100%, 0 100%); color: var(--white);
    font-size: 29px; font-weight: 600; line-height: 63px; padding-left: 20px; }
  .cta-phone { position: absolute; left: 470px; top: 0; height: 63px; display: flex; align-items: center; gap: 10px;
    color: var(--white); font-size: 31px; font-weight: 600; }
  .cta-phone svg { width: 30px; height: 30px; }
</style>
</head>
<body>
<main class="flyer">

  <svg class="hero" viewBox="0 0 810 900" role="img" aria-label="Photo of a large brick house with a dark shingled roof, with round inset photos of roofers at work">
    <defs>
      <linearGradient id="sky" x1="0" y1="0" x2="0" y2="1">
        <stop offset="0" stop-color="#b9d3ea"/>
        <stop offset="0.45" stop-color="#d9e5ee"/>
        <stop offset="0.7" stop-color="#6e6a66"/>
        <stop offset="1" stop-color="#7d9a5a"/>
      </linearGradient>
      <linearGradient id="shingle" x1="0" y1="0" x2="1" y2="1">
        <stop offset="0" stop-color="#9a8270"/>
        <stop offset="1" stop-color="#5f5147"/>
      </linearGradient>
    </defs>
    <polygon points="0,118 810,118 810,530 78,690 0,540" fill="url(#sky)"/>
    <polygon points="0,330 50,330 92,612 420,450 420,500 78,690 0,650" fill="var(--orange)"/>
    <circle cx="678" cy="296" r="137" fill="url(#shingle)" stroke="var(--ring)" stroke-width="9"/>
    <circle cx="413" cy="390" r="98" fill="url(#shingle)" stroke="var(--ring)" stroke-width="8"/>
    <circle cx="234" cy="492" r="82" fill="url(#shingle)" stroke="var(--ring)" stroke-width="7"/>
  </svg>

  <div class="brand"><span class="brand-mark"></span><span class="brand-name">Gable Crest</span></div>
  <div class="website">www.<b>gablecrestmo</b>.com</div>

  <div class="services-tab">What we do?</div>
  <ul class="services">
    <li><svg viewBox="0 0 42 42"><polygon points="21,1 39,11 39,31 21,41 3,31 3,11" fill="var(--orange)"/><path d="M11 23 L21 14 L31 23 M14 21 V30 H28 V21" fill="none" stroke="#fff" stroke-width="2.5"/></svg>Roof Repairs</li>
    <li><svg viewBox="0 0 42 42"><polygon points="21,1 39,11 39,31 21,41 3,31 3,11" fill="var(--orange)"/><path d="M12 28 L28 12 M14 14 L30 30" stroke="#fff" stroke-width="3"/></svg>Replacements</li>
    <li><svg viewBox="0 0 42 42"><polygon points="21,1 39,11 39,31 21,41 3,31 3,11" fill="var(--orange)"/><circle cx="19" cy="19" r="7" fill="none" stroke="#fff" stroke-width="2.5"/><path d="M24 24 L31 31" stroke="#fff" stroke-width="3"/></svg>Roof Inspections</li>
    <li><svg viewBox="0 0 42 42"><polygon points="21,1 39,11 39,31 21,41 3,31 3,11" fill="var(--orange)"/><path d="M13 21 L19 27 L30 15" fill="none" stroke="#fff" stroke-width="3"/></svg>Dry-Seal Certification</li>
  </ul>

  <section class="pitch">
    <h2>HOME INSPECTORS<span>ARE GENERALISTS</span></h2>
    <p>We are roof experts that specialize in diagnosing and fixing roofing problems</p>
  </section>

  <section class="offer">
    <div class="offer-tag">We Offer</div>
    <div class="offer-line one">"DRY SEAL" CERTIFICATION TO</div><br>
    <div class="offer-line two">OFFER PEACE OF MIND TO HOMEOWNERS</div><br>
    <div class="offer-line three">REFERRAL BONUSES FOR REALTORS</div>
  </section>

  <footer class="cta-bar">
    <div class="cta-left">REQUEST A FREE ESTIMATE</div>
    <div class="cta-phone">
      <svg viewBox="0 0 24 24"><path d="M6.6 10.8c1.4 2.8 3.8 5.1 6.6 6.6l2.2-2.2c.3-.3.7-.4 1-.2 1.1.4 2.3.6 3.6.6.6 0 1 .4 1 1V20c0 .6-.4 1-1 1C10.6 21 3 13.4 3 4c0-.6.4-1 1-1h3.5c.6 0 1 .4 1 1 0 1.3.2 2.5.6 3.6.1.3 0 .7-.2 1z" fill="#fff"/></svg>
      (555) 214-ROOF
    </div>
  </footer>

</main>
</body>
</html>
```